Letterhead and Stationary for Construction Company

Lumen Forge needs modern Letterhead, Envelopes and Notepad designs.

Industry/Entity Type

Construction

Colors
f78f20
34a7d8
ffffff

Requirements
Must have
• Modern looking design.

```html
<!DOCTYPE html>
<html lang="en">
<head>
<meta charset="utf-8">
<title>Lumen Forge Stationery</title>
<link href="https://fonts.googleapis.com/css2?family=Poppins:wght@400;600&display=swap" rel="stylesheet">
<style>
  :root{
    --blue:#006db3;
    --orange:#f26f21;
    --paper:#f2f2f2;
    --stage:#d4d4d4;
    --band:#dcdcdc;
    --mark:#e9e9e9;
    --ink:#4a4a4a;
  }
  *{margin:0;padding:0;box-sizing:border-box}
  html,body{width:1200px;height:1041px;overflow:hidden}
  body{background:var(--stage);font-family:"Poppins",sans-serif;position:relative}
  .piece{position:absolute;background:var(--paper);overflow:hidden;box-shadow:0 1px 2px rgba(0,0,0,.18)}
  .piece svg.art{position:absolute;inset:0;width:100%;height:100%}
  .brand{position:absolute;display:flex;align-items:center;gap:5px;font-weight:600;color:var(--blue);white-space:nowrap;line-height:1}
  .brand .dot{border-radius:50%;background:var(--orange);flex:none}
  .contact{position:absolute;font-size:5.4px;line-height:7px;color:var(--ink);font-weight:400;white-space:nowrap}
  .contact .row{display:flex;align-items:center;gap:3px}
  .contact svg{width:5px;height:5px;fill:var(--blue)}

  .folder{left:166px;top:76px;width:417px;height:542px;border-radius:3px}
  .folder .spine{position:absolute;left:24px;top:0;bottom:0;width:2px;background:rgba(0,0,0,.08)}
  .folder .brand{left:0;right:0;top:110px;justify-content:center;font-size:24px;gap:7px}
  .folder .brand .dot{width:13px;height:13px}
  .folder .url{position:absolute;left:0;right:0;top:500px;text-align:center;color:#fff;font-size:7.5px}

  .letterhead{left:615px;top:95px;width:403px;height:523px}
  .letterhead .brand{left:30px;top:42px;font-size:16px}
  .letterhead .brand .dot{width:9px;height:9px}
  .letterhead .contact{left:302px;top:30px}

  .envelope{left:132px;top:645px;width:451px;height:196px}
  .envelope .brand{left:22px;top:32px;font-size:16px}
  .envelope .brand .dot{width:9px;height:9px}
  .envelope .contact{left:22px;top:162px}

  .envelope-back{left:615px;top:645px;width:451px;height:196px}

  .card{left:417px;top:870px;width:167px;height:96px}
  .card .brand{left:15px;top:39px;font-size:8.5px;gap:3px}
  .card .brand .dot{width:5px;height:5px}
  .card .divider{position:absolute;left:90px;top:22px;width:1px;height:48px;background:#cfcfcf}
  .card .contact{left:98px;top:21px;font-size:4.2px;line-height:5.4px}
  .card .name{font-weight:600;color:var(--blue);font-size:4.8px}

  .card-back{left:615px;top:870px;width:167px;height:96px;background:var(--blue)}
  .card-back .brand{left:0;right:0;top:47px;justify-content:center;color:#fff;font-size:13px}
  .card-back .brand .dot{width:7px;height:7px}
  .card-back .url{position:absolute;left:0;right:0;top:67px;text-align:center;color:#fff;font-size:4.5px}
</style>
</head>
<body>

<section class="piece folder">
  <svg class="art" viewBox="0 0 417 542" preserveAspectRatio="none" aria-hidden="true">
    <path d="M0,238 Q150,226 282,222 Q360,224 417,246 L417,542 L0,542Z" fill="var(--orange)"/>
    <path d="M0,254 Q150,234 282,228 Q360,230 417,256 L417,542 L0,542Z" fill="var(--band)"/>
    <path d="M0,268 Q150,238 290,230 Q370,232 417,262 L417,542 L0,542Z" fill="var(--blue)"/>
  </svg>
  <div class="spine"></div>
  <div class="brand"><span class="dot"></span>Lumen Forge</div>
  <p class="url">www.lumenforge.com</p>
</section>

<section class="piece letterhead">
  <svg class="art" viewBox="0 0 403 523" preserveAspectRatio="none" aria-hidden="true">
    <circle cx="201" cy="289" r="128" fill="none" stroke="var(--mark)" stroke-width="28"/>
    <path d="M0,510 Q180,494 300,492 Q360,494 403,512 L403,523 L0,523Z" fill="var(--orange)"/>
    <path d="M120,523 Q220,500 305,498 Q362,500 398,523Z" fill="var(--band)"/>
    <path d="M150,523 Q240,502 310,502 Q366,505 390,523Z" fill="var(--blue)"/>
  </svg>
  <div class="brand"><span class="dot"></span>Lumen Forge</div>
  <div class="contact">
    <div class="row"><svg viewBox="0 0 10 10"><path d="M2,1 L4,1 L5,3 L4,4 Q5,6 6,6 L7,5 L9,6 L9,8 Q5,9 2,5 Q1,3 2,1Z"/></svg>555-210-4400</div>
    <div class="row"><svg viewBox="0 0 10 10"><path d="M2,1 L4,1 L5,3 L4,4 Q5,6 6,6 L7,5 L9,6 L9,8 Q5,9 2,5 Q1,3 2,1Z"/></svg>555-318-0927</div>
    <div class="row"><svg viewBox="0 0 10 10"><rect x="1" y="2" width="8" height="6"/></svg>info@lumenforge.com</div>
    <div class="row"><svg viewBox="0 0 10 10"><circle cx="5" cy="5" r="4"/></svg>www.lumenforge.com</div>
    <div style="margin-top:3px">42 Harbor Line Ave.<br>Suite 12, Eastport Bay</div>
  </div>
</section>

<section class="piece envelope">
  <svg class="art" viewBox="0 0 451 196" preserveAspectRatio="none" aria-hidden="true">
    <circle cx="304" cy="118" r="96" fill="none" stroke="var(--mark)" stroke-width="22"/>
    <path d="M0,184 Q200,168 320,166 Q400,168 451,186 L451,196 L0,196Z" fill="var(--orange)"/>
    <path d="M120,196 Q240,172 330,171 Q400,173 440,196Z" fill="var(--band)"/>
    <path d="M150,196 Q260,174 340,174 Q405,177 430,196Z" fill="var(--blue)"/>
  </svg>
  <div class="brand"><span class="dot"></span>Lumen Forge</div>
  <div class="contact">42 Harbor Line Ave.<br>Suite 12, Eastport Bay</div>
</section>

<section class="piece envelope-back">
  <svg class="art" viewBox="0 0 451 196" preserveAspectRatio="none" aria-hidden="true">
    <path d="M0,0 L451,0 L434,64 L17,64Z" fill="var(--blue)"/>
    <circle cx="226" cy="33" r="11" fill="none" stroke="var(--orange)" stroke-width="3"/>
  </svg>
</section>

<section class="piece card">
  <svg class="art" viewBox="0 0 167 96" preserveAspectRatio="none" aria-hidden="true">
    <path d="M0,90 Q80,84 130,84 Q155,85 167,91 L167,96 L0,96Z" fill="var(--orange)"/>
    <path d="M60,96 Q110,86 135,86 Q156,87 164,96Z" fill="var(--blue)"/>
  </svg>
  <div class="brand"><span class="dot"></span>Lumen Forge</div>
  <div class="divider"></div>
  <div class="contact">
    <div class="name">MARA KELLEN</div>
    <div>Director</div>
    <div style="margin-top:3px">555-210-4400</div>
    <div>555-318-0927</div>
    <div>info@lumenforge.com</div>
    <div>www.lumenforge.com</div>
    <div style="margin-top:2px">42 Harbor Line Ave.<br>Suite 12, Eastport Bay</div>
  </div>
</section>

<section class="piece card-back">
  <div class="brand"><span class="dot"></span>Lumen Forge</div>
  <p class="url">www.lumenforge.com</p>
</section>

</body>
</html>
```